Coastal Sentinels Stationery Design Project

I am looking for a suitable stationary design for my company Coastal Sentinels Pty Ltd (ACN 508 214 396).

The requirements can be better explained by visiting my website
"coastal-sentinels.org"

I will be sending letters to Ministers of State and the Heads of Government Agencies so the theme needs to be formal and serious.

A theme with a shield or similar picking on the "guardian" concept would be appropriate

Target Market(s)

Ministers of State and Department Agency Heads and legal firms, the heads of Trustee Companies as well as Members of Coastal Sentinels

Industry/Entity Type

Government

Requirements
Must have
• Letterhead design is a priority - Business Card secondary

Must include tag line "Shielding your savings when the rest walk away" with a registered trade mark superscript at the end that is an R in a circle {Windows Alt +0174 on numeric keypad or Mac Option +R}.

Must include website address "Coastal-Sentinels.org" plus Email address "coastsentinel@fernmail.net

Company name "Coastal Sentinels Pty. Ltd." and Australian Company Number "ACN 508 214 396" needs to be shown more discretely

Address is "47 Brookfern Lane, Marlow Vale, 3281"
Nice to have
• A watermark is something to be considered

```html
<!DOCTYPE html>
<html lang="en">
<head>
<meta charset="utf-8">
<title>Coastal Sentinels Stationery</title>
<link href="https://fonts.googleapis.com/css2?family=Arimo:wght@400&family=Open+Sans:wght@400&display=swap" rel="stylesheet">
<style>
  :root {
    --backdrop: #5a3521;
    --paper: #ffffff;
    --paper-shade: #ececec;
    --ink: #111111;
    --ink-soft: #9a9a9a;
    --band: #050505;
    --band-text: #f2f2f2;
    --label: #ffffff;
  }
  * { box-sizing: border-box; margin: 0; padding: 0; }
  html, body { width: 1200px; height: 1013px; overflow: hidden; }
  body {
    background: var(--backdrop);
    font-family: "Arimo", Arial, sans-serif;
    color: var(--ink);
    position: relative;
  }
  .sheet {
    position: absolute;
    top: 73px;
    width: 483px;
    height: 626px;
    background: linear-gradient(180deg, var(--paper) 0%, var(--paper-shade) 100%);
    box-shadow: 0 3px 10px rgba(0,0,0,.45);
  }
  .sheet--one { left: 105px; }
  .sheet--two { left: 636px; }

  .brand { position: absolute; text-align: center; white-space: nowrap; }
  .brand__name { font-size: 16px; letter-spacing: .1px; }
  .brand__tagline { font-size: 8.5px; color: var(--ink-soft); margin-top: 1px; }
  .brand__tagline sup { font-size: 5px; }

  .sheet--one .brand { left: 185px; top: 20px; transform: translateX(-50%); }
  .sheet--two .brand { left: 50%; top: 16px; transform: translateX(-50%); }

  .contact {
    position: absolute;
    font-size: 6.5px;
    line-height: 10px;
    white-space: nowrap;
  }
  .contact li { list-style: none; }
  .contact .bullet {
    display: inline-block; width: 4px; height: 4px;
    background: currentColor; margin-right: 3px; vertical-align: 1px;
  }
  .sheet--one .contact {
    left: 355px; top: 19px;
    border-left: 1px solid #777;
    padding-left: 5px;
  }

  .watermark {
    position: absolute;
    left: 162px; top: 174px;
    width: 144px; height: 293px;
    border-radius: 46% 46% 14% 14% / 22% 22% 6% 6%;
    background: linear-gradient(180deg, #e9dcb8 0%, #cfd9c4 30%, #e8c3ba 55%, #e6b5a8 85%, #c9c0b8 100%);
    opacity: .75;
    filter: blur(2px);
  }

  .acn { position: absolute; left: 0; right: 0; text-align: center; font-size: 6.5px; }
  .sheet--one .acn { top: 606px; }
  .sheet--two .acn { top: 608px; }

  .band {
    position: absolute; left: 0; right: 0;
    background: var(--band); color: var(--band-text);
    font-size: 6.5px; line-height: 9.5px;
  }
  .band__address { position: absolute; text-align: right; white-space: nowrap; }
  .band__rule { position: absolute; width: 1px; background: #9a9a9a; }
  .band .contact { color: var(--band-text); }

  .sheet--two .band { top: 576px; height: 29px; }
  .sheet--two .band__address { right: calc(100% - 211px); top: 4px; }
  .sheet--two .band__rule { left: 218px; top: 4px; height: 20px; }
  .sheet--two .band .contact { left: 224px; top: 4px; }

  .option-label {
    position: absolute; top: 714px;
    font-family: "Open Sans", sans-serif;
    font-size: 34px; color: var(--label);
    width: 483px; text-align: center;
  }
  .option-label--one { left: 90px; }
  .option-label--two { left: 622px; }

  .card {
    position: absolute; top: 815px;
    width: 257px; height: 146px;
    border-radius: 8px;
    background: linear-gradient(180deg, #f7f7f7 0%, #ffffff 40%, #e9e9e9 100%);
    box-shadow: 0 3px 8px rgba(0,0,0,.45);
    overflow: hidden;
  }
  .card--front { left: 336px; }
  .card--back { left: 627px; }
  .card .brand { left: 50%; transform: translateX(-50%); }
  .card--front .brand { top: 29px; }
  .card--back .brand { top: 54px; }
  .card .brand__name { font-size: 15px; }
  .card .brand__tagline { font-size: 8px; }

  .card--front .band { top: 84px; height: 29px; }
  .card--front .band__address { right: calc(100% - 100px); top: 5px; }
  .card--front .band__rule { left: 106px; top: 4px; height: 21px; }
  .card--front .band .contact { left: 111px; top: 5px; }
  .card--front .acn { top: 127px; }

  .card__web {
    position: absolute; left: 0; right: 0; top: 120px;
    text-align: center; font-size: 6.5px; letter-spacing: 1.3px; color: #555;
  }
</style>
</head>
<body>

  <section class="sheet sheet--one" aria-label="Letterhead option 1">
    <div class="brand">
      <p class="brand__name">Coastal Sentinels Pty Ltd.</p>
      <p class="brand__tagline">Shielding your savings when the rest walk away<sup>®</sup></p>
    </div>
    <ul class="contact">
      <li>47 Brookfern Lane Marlow Vale, 3281</li>
      <li><span class="bullet"></span>coastsentinel@fernmail.net</li>
      <li><span class="bullet"></span>www.Coastal-Sentinels.org</li>
    </ul>
    <div class="watermark" role="img" aria-label="Faint watermark of a carved guardian figurine"></div>
    <p class="acn">ACN 508 214 396</p>
  </section>

  <section class="sheet sheet--two" aria-label="Letterhead option 2">
    <div class="brand">
      <p class="brand__name">Coastal Sentinels Pty Ltd.</p>
      <p class="brand__tagline">Shielding your savings when the rest walk away<sup>®</sup></p>
    </div>
    <div class="band">
      <p class="band__address">47 Brookfern Lane<br>Marlow Vale, 3281</p>
      <span class="band__rule"></span>
      <ul class="contact">
        <li><span class="bullet"></span>coastsentinel@fernmail.net</li>
        <li><span class="bullet"></span>www.Coastal-Sentinels.org</li>
      </ul>
    </div>
    <p class="acn">ACN 508 214 396</p>
  </section>

  <p class="option-label option-label--one">Option-1</p>
  <p class="option-label option-label--two">Option-2</p>

  <section class="card card--front" aria-label="Business card front">
    <div class="brand">
      <p class="brand__name">Coastal Sentinels Pty Ltd.</p>
      <p class="brand__tagline">Shielding your savings when the rest walk away<sup>®</sup></p>
    </div>
    <div class="band">
      <p class="band__address">47 Brookfern Lane<br>Marlow Vale, 3281</p>
      <span class="band__rule"></span>
      <ul class="contact">
        <li><span class="bullet"></span>coastsentinel@fernmail.net</li>
        <li><span class="bullet"></span>www.Coastal-Sentinels.org</li>
      </ul>
    </div>
    <p class="acn">ACN 508 214 396</p>
  </section>

  <section class="card card--back" aria-label="Business card back">
    <div class="brand">
      <p class="brand__name">Coastal Sentinels Pty Ltd.</p>
      <p class="brand__tagline">Shielding your savings when the rest walk away<sup>®</sup></p>
    </div>
    <p class="card__web">www.Coastal-Sentinels.org</p>
  </section>

</body>
</html>
```